Construction material supplies company business card ****

1. Full company name “K R Mortar Works Ltd”
I am after a Business card design for the company as a whole. We are better known in Solomon Islands as “K R Mortar” for short.

We are a building materials supplier of
Ready Mixed Concrete, Bricks and Blocks,
Quarry products- gravel, aggregates, sand etc.
Cement distributor/retailer of reputable brands.
Other prefab concrete products. Culverts, wave breakers, concrete retaining blocks etc.

2. Competitive Advantage over Competition: Quality, efficient, professional, dependable, reliable

3. We want people to feel trust worthy, high quality, strong when they see our brand

5. No preference to color. Maybe more sturdy and corporate. Not fancy.

Industry/Entity Type

CONSTRUCTION SUPPLY

Contact Information for Business Card

Name, Position, office phone mob phone, email

Requirements
Must have
• the company logo
Nice to have
• would like to see a mixture of designs, of with logo only and also with simple graphic designs to bring out the company whilst still have the strong sturdy professional feeling

```html
<!DOCTYPE html>
<html lang="en">
<head>
<meta charset="utf-8">
<title>K R Mortar — Business Card</title>
<link href="https://fonts.googleapis.com/css2?family=Audiowide&family=Poppins:wght@400;500&display=swap" rel="stylesheet">
<style>
  :root {
    --stage: #2b2c2e;
    --concrete: #e6e7e8;
    --concrete-dark: #cfd1d3;
    --navy: #17457a;
    --sky: #3f8fd8;
    --white: #ffffff;
  }
  * { box-sizing: border-box; margin: 0; padding: 0; }
  html, body { width: 1200px; height: 900px; overflow: hidden; }
  body { background: var(--stage); position: relative; font-family: "Poppins", sans-serif; }

  .card {
    position: absolute; left: 250px; width: 700px; height: 400px;
    border-radius: 26px; overflow: hidden;
    background: radial-gradient(ellipse at 30% 20%, var(--concrete) 0%, var(--concrete-dark) 100%);
  }
  .card-back { top: 33px; }
  .card-front { top: 467px; }
  .card-shapes { position: absolute; inset: 0; width: 100%; height: 100%; }

  .display { font-family: "Audiowide", sans-serif; text-transform: uppercase; }

  /* back */
  .back-brand { position: absolute; left: 200px; top: 62px; display: flex; align-items: center; gap: 16px; }
  .brand-square { width: 30px; height: 30px; background: var(--navy); }
  .back-brand .brand-name { color: var(--navy); font-size: 42px; letter-spacing: 1px; }
  .service-list { position: absolute; left: 56px; top: 222px; right: 24px; list-style: none; color: var(--white); font-size: 14px; letter-spacing: 0.5px; line-height: 26px; }
  .service-list li::before { content: ""; display: inline-block; width: 9px; height: 9px; background: var(--sky); margin-right: 10px; vertical-align: middle; }
  .service-list .service-heading { color: var(--sky); font-size: 17px; }
  .service-list .service-heading::before { display: none; }
  .service-row { white-space: nowrap; }
  .service-row span { margin-right: 14px; }
  .service-row span::before { content: ""; display: inline-block; width: 9px; height: 9px; background: var(--sky); margin-right: 10px; vertical-align: middle; }
  .service-list li.service-row::before { display: none; }

  /* front */
  .front-name { position: absolute; left: 42px; top: 108px; color: var(--navy); font-size: 56px; letter-spacing: 1px; }
  .front-mark { position: absolute; right: 44px; top: 46px; display: flex; align-items: center; gap: 12px; }
  .front-mark .brand-name { color: var(--navy); font-size: 34px; }
  .person { position: absolute; left: 44px; top: 190px; }
  .person-name { color: var(--navy); font-size: 22px; letter-spacing: 1px; }
  .person-role { color: var(--sky); font-size: 15px; margin-top: 2px; }
  .contact-list { position: absolute; left: 44px; top: 292px; list-style: none; color: var(--white); font-size: 17px; line-height: 27px; }
  .contact-list li { display: flex; align-items: center; gap: 12px; }
  .contact-list svg { width: 16px; height: 16px; flex: none; }
  .address { position: absolute; right: 40px; top: 222px; text-align: right; color: var(--white); font-size: 16px; line-height: 25px; font-style: normal; }
</style>
</head>
<body>

<section class="card card-back">
  <svg class="card-shapes" viewBox="0 0 700 400" preserveAspectRatio="none" aria-hidden="true">
    <path d="M0 198 C180 142 420 142 700 142 L700 400 L0 400 Z" fill="var(--sky)"/>
    <path d="M0 210 C180 156 420 156 700 156 L700 400 L0 400 Z" fill="var(--navy)"/>
  </svg>
  <div class="back-brand">
    <span class="brand-square"></span>
    <span class="brand-name display">K R Mortar</span>
  </div>
  <ul class="service-list display">
    <li>Ready mixed concrete</li>
    <li>Bricks and blocks,</li>
    <li>Quarry products- gravel, aggregates, sand etc.</li>
    <li>Cement distributor/retailer of reputable brands.</li>
    <li class="service-heading">Other prefab concrete products</li>
    <li class="service-row"><span>Culverts</span><span>Wave breakers</span><span>Concrete retaining blocks etc.</span></li>
  </ul>
</section>

<section class="card card-front">
  <svg class="card-shapes" viewBox="0 0 700 400" preserveAspectRatio="none" aria-hidden="true">
    <path d="M0 282 L700 186 L700 400 L0 400 Z" fill="var(--navy)"/>
    <line x1="0" y1="394" x2="700" y2="368" stroke="var(--white)" stroke-width="2"/>
  </svg>
  <div class="front-mark">
    <span class="brand-square"></span>
    <span class="brand-name display">K R Mortar</span>
  </div>
  <h1 class="front-name display">K R Mortar</h1>
  <div class="person">
    <p class="person-name display">Daniel Whitmore</p>
    <p class="person-role display">CEO/Founder</p>
  </div>
  <ul class="contact-list">
    <li>
      <svg viewBox="0 0 16 16"><path d="M3 1.5 L6 1.5 L7 5 L5 6.5 C6 9 7.5 10.5 9.5 11 L11 9 L14.5 10 L14.5 13 C14.5 14 13.5 14.5 12.5 14.5 C6.5 14 2 9.5 1.5 3.5 C1.5 2.5 2 1.5 3 1.5 Z" fill="var(--white)"/></svg>
      <span>677-24-5108</span>
    </li>
    <li>
      <svg viewBox="0 0 16 16"><rect x="1" y="3" width="14" height="10" fill="var(--white)"/><path d="M1 3 L8 9 L15 3" fill="none" stroke="var(--navy)" stroke-width="1.4"/></svg>
      <span>daniel@krmortarmail.com</span>
    </li>
    <li>
      <svg viewBox="0 0 16 16" fill="none" stroke="var(--white)" stroke-width="1.3"><circle cx="8" cy="8" r="6.5"/><ellipse cx="8" cy="8" rx="2.8" ry="6.5"/><line x1="1.5" y1="8" x2="14.5" y2="8"/></svg>
      <span>www.krmortarworks.com</span>
    </li>
  </ul>
  <address class="address">
    18 Harbour Road<br>
    Suite 2, Honiara<br>
    Solomon Islands
  </address>
</section>

</body>
</html>
```